Norvel Hand Wash

Design hand washes. Total 12 variants to be designed.

Variants name are:

1) MILK &OLIVE
2) Shea Butter
3) Hidden Dawn
4) Cream and Peach
5) Milk and Honey
6) Amber Whisper
7) Bakhour
8) Musk
9) White Oud
10) Black Oud
11) Rose Oud
12) Oud & Sandalwood

Labels can be on transparent sticker or background colors. All variants will be differentiated by fragrances and color. Bottle will be transparent. Pumps used for dispensing will be in Black or Transparent Color.

Designers can initially present designs of 4-5 variants initially. Later based on feedback, they can work out on more.

Bottle is 400ml and shape is rectangle. Ignore the size on bottle picture. Bottle keyline is attached.

Target Market(s)

B+, B, C+

Requirements
Must have
• Some relation to the variant names

```html
<!DOCTYPE html>
<html lang="en">
<head>
<meta charset="utf-8">
<title>Norvel Hand Wash – Range</title>
<link href="https://fonts.googleapis.com/css2?family=Open+Sans:wght@600;700&family=Rancho&display=swap" rel="stylesheet">
<style>
  :root{
    --bg:#eeeeef;
    --pump:#f4f5f6;
    --pump-edge:#d5d8db;
    --ink-brand:#4a3f9a;
    --lilac:#c79fdc; --lilac-deep:#a974c6; --lilac-ink:#9a5cb8;
    --sage:#a9d39c; --sage-deep:#86bd78; --sage-ink:#5f8f3e;
    --peach:#f7b996; --peach-deep:#ee9e78; --peach-ink:#d4773b;
    --honey:#f8b620; --honey-deep:#f0a000; --honey-ink:#c46a12;
    --white:#ffffff;
  }
  *{box-sizing:border-box;margin:0;padding:0}
  html,body{width:1200px;height:1200px;overflow:hidden;background:var(--bg)}
  .canvas{
    width:1200px;height:1200px;position:relative;overflow:hidden;
    background:var(--bg);
    display:flex;justify-content:center;align-items:flex-start;gap:34px;
    padding:0 40px;
  }
  .bottle{width:250px;position:relative;display:flex;flex-direction:column;align-items:center}
  .bottle--lilac{margin-top:160px;--c:var(--lilac);--cd:var(--lilac-deep);--ink:var(--lilac-ink)}
  .bottle--sage{margin-top:225px;--c:var(--sage);--cd:var(--sage-deep);--ink:var(--sage-ink)}
  .bottle--peach{margin-top:150px;--c:var(--peach);--cd:var(--peach-deep);--ink:var(--peach-ink)}
  .bottle--honey{margin-top:95px;--c:var(--honey);--cd:var(--honey-deep);--ink:var(--honey-ink)}

  .pump{display:block;width:250px;height:230px}
  .body{
    width:250px;height:580px;margin-top:-4px;border-radius:46px 46px 30px 30px;
    background:linear-gradient(90deg,var(--cd) 0%,var(--c) 18%,var(--c) 80%,var(--cd) 100%);
    position:relative;overflow:hidden;
  }
  .label{
    position:absolute;left:20px;right:20px;top:80px;bottom:28px;
    border-radius:26px;background:rgba(255,255,255,.2);
    border:1px solid rgba(255,255,255,.4);overflow:hidden;
    display:flex;flex-direction:column;align-items:center;
  }
  .ribbon{
    position:absolute;top:26px;left:-46px;width:190px;transform:rotate(-45deg);
    background:rgba(255,255,255,.3);text-align:center;
    font:700 12px/20px "Open Sans",sans-serif;color:var(--white);letter-spacing:.5px;
  }
  .brand{
    margin-top:74px;width:190px;height:100px;border-radius:50%;
    background:radial-gradient(ellipse at center,rgba(255,255,255,.95) 40%,rgba(255,255,255,0) 72%);
    display:flex;flex-direction:column;align-items:center;justify-content:center;
  }
  .brand__name{display:flex;align-items:center;gap:6px;font:700 40px/1 "Open Sans",sans-serif;color:var(--ink-brand)}
  .brand__dot{width:10px;height:10px;border-radius:50%;background:var(--ink-brand)}
  .brand__tag{font:600 10px/1 "Open Sans",sans-serif;color:var(--ink-brand);margin-top:4px;align-self:flex-end;margin-right:34px}
  .foam{
    position:absolute;left:0;right:0;bottom:0;height:210px;
    background:radial-gradient(ellipse at 50% 40%,rgba(255,255,255,.55),rgba(255,255,255,.2) 70%);
    border-radius:60px 60px 0 0;
  }
  .variant{position:absolute;left:0;right:0;bottom:22px;display:flex;flex-direction:column;align-items:center}
  .variant__icon{width:50px;height:44px;border-radius:10px;background:rgba(255,255,255,.5);margin-bottom:8px}
  .variant__name{font:400 30px/1 "Rancho",cursive;color:var(--ink)}
  .variant__type{font:700 14px/1.3 "Open Sans",sans-serif;color:var(--ink);letter-spacing:.3px}
  .variant__size{font:700 13px/1 "Open Sans",sans-serif;color:var(--ink);margin-top:22px}
</style>
</head>
<body>
<main class="canvas">

  <section class="bottle bottle--lilac">
    <svg class="pump" viewBox="0 0 250 230" aria-hidden="true">
      <rect x="115" y="10" width="110" height="18" rx="6" fill="var(--pump)" stroke="var(--pump-edge)"/>
      <rect x="102" y="8" width="46" height="92" rx="6" fill="var(--pump)" stroke="var(--pump-edge)"/>
      <rect x="82" y="95" width="86" height="100" rx="10" fill="var(--pump)" stroke="var(--pump-edge)"/>
      <rect x="92" y="192" width="66" height="40" fill="rgba(255,255,255,.5)" stroke="var(--pump-edge)"/>
    </svg>
    <div class="body">
      <div class="label">
        <div class="ribbon">NEW FORMULA</div>
        <div class="brand"><div class="brand__name"><span class="brand__dot"></span>Norvel</div><div class="brand__tag">Air Freshener</div></div>
        <div class="foam" role="img" aria-label="Soft bubbles and foam decoration"></div>
        <div class="variant">
          <div class="variant__icon" role="img" aria-label="Heart swirl icon"></div>
          <div class="variant__name">Hidden Dawn</div>
          <div class="variant__type">HAND WASH</div>
          <div class="variant__size">400ml</div>
        </div>
      </div>
    </div>
  </section>

  <section class="bottle bottle--sage">
    <svg class="pump" viewBox="0 0 250 230" aria-hidden="true">
      <rect x="115" y="10" width="110" height="18" rx="6" fill="var(--pump)" stroke="var(--pump-edge)"/>
      <rect x="102" y="8" width="46" height="92" rx="6" fill="var(--pump)" stroke="var(--pump-edge)"/>
      <rect x="82" y="95" width="86" height="100" rx="10" fill="var(--pump)" stroke="var(--pump-edge)"/>
      <rect x="92" y="192" width="66" height="40" fill="rgba(255,255,255,.5)" stroke="var(--pump-edge)"/>
    </svg>
    <div class="body">
      <div class="label">
        <div class="ribbon">NEW FORMULA</div>
        <div class="brand"><div class="brand__name"><span class="brand__dot"></span>Norvel</div><div class="brand__tag">Air Freshener</div></div>
        <div class="foam" role="img" aria-label="Soft bubbles and foam decoration"></div>
        <div class="variant">
          <div class="variant__icon" role="img" aria-label="Milk jug and olive icon"></div>
          <div class="variant__name">Milk &amp; Olive</div>
          <div class="variant__type">HAND WASH</div>
          <div class="variant__size">400ml</div>
        </div>
      </div>
    </div>
  </section>

  <section class="bottle bottle--peach">
    <svg class="pump" viewBox="0 0 250 230" aria-hidden="true">
      <rect x="115" y="10" width="110" height="18" rx="6" fill="var(--pump)" stroke="var(--pump-edge)"/>
      <rect x="102" y="8" width="46" height="92" rx="6" fill="var(--pump)" stroke="var(--pump-edge)"/>
      <rect x="82" y="95" width="86" height="100" rx="10" fill="var(--pump)" stroke="var(--pump-edge)"/>
      <rect x="92" y="192" width="66" height="40" fill="rgba(255,255,255,.5)" stroke="var(--pump-edge)"/>
    </svg>
    <div class="body">
      <div class="label">
        <div class="ribbon">NEW FORMULA</div>
        <div class="brand"><div class="brand__name"><span class="brand__dot"></span>Norvel</div><div class="brand__tag">Air Freshener</div></div>
        <div class="foam" role="img" aria-label="Soft bubbles and foam decoration"></div>
        <div class="variant">
          <div class="variant__icon" role="img" aria-label="Cream swirl and peach icon"></div>
          <div class="variant__name">Cream &amp; Peach</div>
          <div class="variant__type">HAND WASH</div>
          <div class="variant__size">400ml</div>
        </div>
      </div>
    </div>
  </section>

  <section class="bottle bottle--honey">
    <svg class="pump" viewBox="0 0 250 230" aria-hidden="true">
      <rect x="115" y="10" width="110" height="18" rx="6" fill="var(--pump)" stroke="var(--pump-edge)"/>
      <rect x="102" y="8" width="46" height="92" rx="6" fill="var(--pump)" stroke="var(--pump-edge)"/>
      <rect x="82" y="95" width="86" height="100" rx="10" fill="var(--pump)" stroke="var(--pump-edge)"/>
      <rect x="92" y="192" width="66" height="40" fill="rgba(255,255,255,.5)" stroke="var(--pump-edge)"/>
    </svg>
    <div class="body">
      <div class="label">
        <div class="ribbon">NEW FORMULA</div>
        <div class="brand"><div class="brand__name"><span class="brand__dot"></span>Norvel</div><div class="brand__tag">Air Freshener</div></div>
        <div class="foam" role="img" aria-label="Soft bubbles and foam decoration"></div>
        <div class="variant">
          <div class="variant__icon" role="img" aria-label="Milk jug and honey dipper icon"></div>
          <div class="variant__name">Milk &amp; Honey</div>
          <div class="variant__type">HAND WASH</div>
          <div class="variant__size">400ml</div>
        </div>
      </div>
    </div>
  </section>

</main>
</body>
</html>
```